Brightstone Roofing Business Card

This is my current business card. But I’d like to make some changes. Somewhere on the card I’d like to list some of the services we offer. Maybe on the back? But I’d still like to keep the red. White and black modern look.

-residential & commercial roofing
-Roof Repairs & Maintenance
-Storm Damage & Insurance Claims specialist
-Christmas Lights and permanent Christmas lights
Fencing. Windows. Gutters. Siding. Sheetrock, painting.

```html
<!DOCTYPE html>
<html lang="en">
<head>
<meta charset="utf-8">
<title>Brightstone Roofing Business Card</title>
<link rel="stylesheet" href="https://fonts.googleapis.com/css2?family=Michroma&family=Arimo:wght@400;700&display=swap">
<style>
  :root {
    --stage: #3b3b3d;
    --card-black: #232325;
    --emboss: #3a3a3e;
    --card-white: #ffffff;
    --brand-red: #e31b1b;
    --ink: #1b1b1b;
    --muted: #8a8a8a;
    --light-text: #cfcfcf;
    --divider: #cfcfcf;
    --divider-dark: #3c3c40;
  }
  * { box-sizing: border-box; margin: 0; padding: 0; }
  html, body {
    width: 1200px; height: 689px; overflow: hidden;
    background: var(--stage);
  }
  .stage {
    position: relative; width: 1200px; height: 689px;
    display: flex; align-items: center; justify-content: center; gap: 50px;
  }
  .card {
    width: 530px; height: 303px; border-radius: 18px;
    position: relative; overflow: hidden;
    border-bottom: 3px solid var(--brand-red);
    box-shadow: 0 18px 40px rgba(0,0,0,0.35);
  }

  /* back */
  .card--back {
    background: var(--card-black);
    display: flex; align-items: center;
    padding: 0 30px 0 24px;
  }
  .back-brand {
    width: 180px; flex: none;
    display: flex; flex-direction: column; align-items: center; gap: 14px;
  }
  .back-mark {
    width: 72px; height: 72px; border-radius: 50%;
    background: var(--emboss);
  }
  .back-name {
    font-family: "Michroma", sans-serif;
    color: #55555b;
    font-size: 15px; line-height: 1.3; letter-spacing: 0.5px;
    text-align: center; text-transform: uppercase;
  }
  .back-divider {
    width: 1px; height: 180px; flex: none; margin: 0 24px 0 14px;
    background: linear-gradient(var(--card-black), var(--divider-dark), var(--card-black));
  }
  .services { flex: 1; min-width: 0; }
  .services-title {
    font-family: "Michroma", sans-serif;
    color: var(--brand-red);
    font-size: 13px; letter-spacing: 1px; text-transform: uppercase;
    margin-bottom: 14px;
  }
  .services-list { list-style: none; }
  .service-item {
    position: relative; padding-left: 14px;
    font-family: "Arimo", sans-serif;
    color: var(--light-text); font-size: 11.5px; line-height: 1.35;
    margin-bottom: 8px;
  }
  .service-item::before {
    content: ""; position: absolute; left: 0; top: 5px;
    width: 5px; height: 5px; background: var(--brand-red);
  }
  .service-item:last-child { margin-bottom: 0; }

  /* front */
  .card--front {
    background: var(--card-white);
    display: flex; align-items: center;
  }
  .front-brand {
    width: 245px; height: 100%;
    display: flex; flex-direction: column; align-items: center; justify-content: center; gap: 12px;
  }
  .brand-dot {
    width: 62px; height: 62px; border-radius: 50%;
    background: var(--brand-red);
  }
  .brand-name {
    font-family: "Michroma", sans-serif;
    color: var(--ink);
    font-size: 15px; line-height: 1.3; text-align: center;
    text-transform: uppercase; letter-spacing: 0.5px;
  }
  .divider {
    width: 1px; height: 170px;
    background: linear-gradient(var(--card-white), var(--divider), var(--card-white));
  }
  .front-details { padding-left: 28px; }
  .person-name {
    font-family: "Michroma", sans-serif;
    color: var(--brand-red);
    font-size: 22px; letter-spacing: 1px; text-transform: uppercase;
  }
  .person-role {
    font-family: "Arimo", sans-serif;
    color: var(--muted); font-size: 13px; margin-top: 2px;
  }
  .contact-list { list-style: none; margin-top: 22px; }
  .contact-item {
    display: flex; align-items: center; gap: 10px;
    font-family: "Arimo", sans-serif;
    color: var(--ink); font-size: 13px; line-height: 1.6;
  }
  .contact-icon { width: 11px; height: 11px; fill: var(--brand-red); flex: none; }
</style>
</head>
<body>
<main class="stage">
  <section class="card card--back" aria-label="Card back">
    <div class="back-brand">
      <span class="back-mark"></span>
      <span class="back-name">Brightstone<br>Roofing Co.</span>
    </div>
    <div class="back-divider"></div>
    <div class="services">
      <h2 class="services-title">Our Services</h2>
      <ul class="services-list">
        <li class="service-item">Residential &amp; Commercial Roofing</li>
        <li class="service-item">Roof Repairs &amp; Maintenance</li>
        <li class="service-item">Storm Damage &amp; Insurance Claims Specialist</li>
        <li class="service-item">Christmas Lights &amp; Permanent Christmas Lights</li>
        <li class="service-item">Fencing · Windows · Gutters · Siding · Sheetrock · Painting</li>
      </ul>
    </div>
  </section>

  <section class="card card--front" aria-label="Card front">
    <div class="front-brand">
      <span class="brand-dot"></span>
      <span class="brand-name">Brightstone<br>Roofing Co.</span>
    </div>
    <div class="divider"></div>
    <div class="front-details">
      <h1 class="person-name">Dean Marsh</h1>
      <p class="person-role">Owner</p>
      <ul class="contact-list">
        <li class="contact-item">
          <svg class="contact-icon" viewBox="0 0 24 24"><path d="M6.6 10.8a15.1 15.1 0 0 0 6.6 6.6l2.2-2.2c.3-.3.7-.4 1-.2 1.1.4 2.3.6 3.6.6.6 0 1 .4 1 1V20c0 .6-.4 1-1 1A17 17 0 0 1 3 4c0-.6.4-1 1-1h3.5c.6 0 1 .4 1 1 0 1.3.2 2.5.6 3.6.1.3 0 .7-.2 1z"/></svg>
          555.014.2290
        </li>
        <li class="contact-item">
          <svg class="contact-icon" viewBox="0 0 24 24"><path d="M2 5h20v14H2z"/><path d="M3 6l9 7 9-7" fill="none" stroke="#fff" stroke-width="1.6"/></svg>
          dean@brightstoneroofing.co
        </li>
        <li class="contact-item">
          <svg class="contact-icon" viewBox="0 0 24 24"><circle cx="12" cy="12" r="10"/><path d="M2 12h20M12 2c3 3 3 17 0 20M12 2c-3 3-3 17 0 20" fill="none" stroke="#fff" stroke-width="1.4"/></svg>
          www.brightstoneroofing.co
        </li>
      </ul>
    </div>
  </section>
</main>
</body>
</html>
```